Business Stationery - New Business card design

We are looking for some new business stationery, including business cards (double sided), compliment slips & letterheads for our offices in the UK, Ireland, North Carolina (US) & our Holdings company.

We are open to all ideas; however we are ideally looking for something that does not look corporate.

Our website is www.talvonahumancapital.example – this is the style of branding that we are currently using.

Here is some of the information that should be included;

Business Cards

Front
Logo
Name – Desmond Varrow
Job Title - Director
Direct line number - +353 (0)1 468 2071
Office number - +353 (0)1 482 6150
Email address – d.varrow@talvonahc.example
Website address – www.talvonahumancapital.example

Back
Logo
‘Specialists in IT Recruitment’
LinkedIn – Talvona Human Capital
Twitter - @talvonahire
An image included – possibly ‘Image 1’ attached?

Letterheads & Compliment slips

UK (A4 size)
Logo
Phone numbers for the various offices;
London: +44 (0)20 7961 3327
Belfast: +44 (0)28 9037 6615
Dublin: +353 (0)1 482 6150
Raleigh, NC: +1 919 642 1357
Address: 2nd Floor, 118 Marlowe Street, London W1C 4PJ
Email: info@talvonahc.example
Website: www.talvonahumancapital.example
Social media icons for LinkedIn & Twitter
Talvona Human Capital Registered in England & Wales No. 6815337 VAT No. 871342609

Ireland (A4 size)
Logo
Address: 4-7 Corran Street, Dublin 2 D02 KX58, Ireland
Email: info@talvonahc.example
Talvona Human Capital (Ireland) Registered in Ireland No. 624903 VAT No. 7182635KK

USA (letter size)

Logo
Address: 542 N. Pellam Street, Raleigh, North Carolina 27605, United States
Email: info@talvonahc.example
Talvona Human Capital Inc. Registered in the State of North Carolina No. 2640917

Holdings (A4 size)

Logo
Address: 58 Fenwick Street, Belfast BT27JD
Email: info@talvonahc.example
Talvona Human Capital (Holdings) Ltd Registered in Northern Ireland No. NI583076

Target Market(s)

IT Professionals

Industry/Entity Type

It Professional

Contact Information for Business Card

Front
Logo
Name – Desmond Varrow
Job Title - Director

Back
Logo
Twitter - @talvonahire

```html
<!DOCTYPE html>
<html lang="en">
<head>
<meta charset="utf-8">
<title>Talvona Human Capital – Business Cards</title>
<link rel="stylesheet" href="https://fonts.googleapis.com/css2?family=Cinzel:wght@500;600&family=Arimo:wght@400&display=swap">
<style>
  :root {
    --brand-blue: #0b5aa8;
    --brand-green: #6cb026;
    --ink: #4a4a4a;
    --rule: #c9ccd1;
    --page: #e9ebee;
    --white: #ffffff;
  }
  * { box-sizing: border-box; margin: 0; padding: 0; }
  html, body { width: 1200px; height: 1015px; overflow: hidden; background: var(--page); }
  .canvas { position: relative; width: 1200px; height: 1015px; }

  .card {
    position: absolute;
    left: 210px;
    width: 780px;
    height: 446px;
    overflow: hidden;
    box-shadow: 0 6px 18px rgba(0,0,0,.18);
  }
  .card--back { top: 40px; background: var(--brand-blue); color: var(--white); }
  .card--front { top: 529px; background: var(--white); }

  .wordmark {
    font-family: "Cinzel", serif;
    font-weight: 600;
    letter-spacing: 1px;
    line-height: 1;
    white-space: nowrap;
  }

  /* Back */
  .back-brand { position: absolute; right: 60px; top: 70px; text-align: left; }
  .back-brand .wordmark { font-size: 36px; color: var(--white); }
  .tagline { font-family: "Arimo", sans-serif; font-size: 21px; margin-top: 14px; color: var(--white); }
  .illustration {
    position: absolute; left: 0; bottom: 0; width: 400px; height: 250px;
    background: linear-gradient(135deg, #cfe7ea 0%, #e6eef0 45%, #e4574b 75%, #f0c545 100%);
    border-top-right-radius: 30px;
  }
  .social { position: absolute; left: 470px; top: 320px; font-family: "Arimo", sans-serif; font-size: 20px; list-style: none; }
  .social li { display: flex; align-items: center; gap: 10px; margin-bottom: 8px; white-space: nowrap; }
  .social .dot { width: 22px; height: 22px; border-radius: 50%; background: var(--white); flex: none; }

  /* Front */
  .front-brand { position: absolute; right: 60px; top: 70px; }
  .front-brand .wordmark { font-size: 44px; color: var(--brand-blue); }
  .divider { position: absolute; left: 60px; right: 60px; top: 220px; border-top: 1px solid var(--rule); }
  .person { position: absolute; left: 60px; top: 245px; }
  .person__name { font-family: "Cinzel", serif; font-weight: 600; font-size: 32px; color: var(--brand-blue); line-height: 1.1; }
  .person__role { font-family: "Arimo", sans-serif; font-size: 24px; color: var(--brand-green); letter-spacing: 1px; }
  .contacts { position: absolute; top: 345px; font-family: "Arimo", sans-serif; font-size: 20px; color: var(--ink); list-style: none; }
  .contacts--phone { left: 60px; }
  .contacts--web { left: 380px; }
  .contacts li { display: flex; align-items: center; gap: 10px; margin-bottom: 10px; white-space: nowrap; }
  .contacts .note { color: var(--brand-blue); }
  .icon { width: 26px; height: 26px; flex: none; }
</style>
</head>
<body>
<main class="canvas">

  <section class="card card--back" aria-label="Business card back">
    <div class="back-brand">
      <div class="wordmark">Talvona Human Capital</div>
      <p class="tagline">Specialists in IT Recruitment</p>
    </div>
    <div class="illustration" role="img" aria-label="Illustrated city of office buildings with clouds and an aeroplane"></div>
    <ul class="social">
      <li><span class="dot"></span>@talvonahire</li>
      <li><span class="dot"></span>Talvona Human Capital</li>
    </ul>
  </section>

  <section class="card card--front" aria-label="Business card front">
    <div class="front-brand">
      <div class="wordmark">Talvona Human Capital</div>
    </div>
    <div class="divider"></div>
    <div class="person">
      <h1 class="person__name">DESMOND VARROW</h1>
      <p class="person__role">Director</p>
    </div>
    <ul class="contacts contacts--phone">
      <li>
        <svg class="icon" viewBox="0 0 26 26"><circle cx="13" cy="13" r="13" fill="var(--brand-blue)"/><path d="M9 7c1 0 2 2.5 2 3s-1 1-1 1.5 2.5 3.5 3.5 3.5 1-1 1.5-1 3 1 3 2-1.5 2-2.5 2C10 18 8 12 8 9c0-1 .5-2 1-2z" fill="#fff"/></svg>
        +353 (0)1 468 2071 <span class="note">(Direct)</span>
      </li>
      <li>
        <svg class="icon" viewBox="0 0 26 26"><circle cx="13" cy="13" r="13" fill="var(--brand-blue)"/><path d="M9 7c1 0 2 2.5 2 3s-1 1-1 1.5 2.5 3.5 3.5 3.5 1-1 1.5-1 3 1 3 2-1.5 2-2.5 2C10 18 8 12 8 9c0-1 .5-2 1-2z" fill="#fff"/></svg>
        +353 (0)1 482 6150
      </li>
    </ul>
    <ul class="contacts contacts--web">
      <li>
        <svg class="icon" viewBox="0 0 26 26"><circle cx="13" cy="13" r="13" fill="var(--brand-blue)"/><rect x="7" y="9" width="12" height="8" fill="none" stroke="#fff" stroke-width="1.5"/><path d="M7 9l6 5 6-5" fill="none" stroke="#fff" stroke-width="1.5"/></svg>
        d.varrow@talvonahc.example
      </li>
      <li>
        <svg class="icon" viewBox="0 0 26 26"><circle cx="13" cy="13" r="13" fill="var(--brand-blue)"/><circle cx="13" cy="13" r="6" fill="none" stroke="#fff" stroke-width="1.5"/><path d="M7 13h12M13 7c-3 3-3 9 0 12M13 7c3 3 3 9 0 12" fill="none" stroke="#fff" stroke-width="1.2"/></svg>
        www.talvonahumancapital.example
      </li>
    </ul>
  </section>

</main>
</body>
</html>
```